Design a cool print brochure for an NGO / Give your work a global impact!!

Hi,
I provide a full design brief (below, please scroll) and a mood board (attached) to help you visualize inside my head.. ;-)
I am also available to help and have worked many years in advertising; we will understand each other.
Objective:
To design an A4 folded in two presentation brochure for a non-profit consulting agency called Vantor.
Vantor works in sustainability and international development = working with NGO’s, governments and private sector on global issues such as global warming, education for all etc.
Strategy:
This document is a first step in developing a communication strategy. It will be distributed during a major international event called the Meridian Outreach Forum.
Objective:
The double objective of the brochure is:
a) to inform the recipient of what Vantor is, in the shortest time possible.
b) to showcase relevant projects to demonstrate Vantor experience and expertise.
Target:
Main target:
Existing Vantor contacts, such as members of development organizations, NGOs, private sector foundations (CSR), regional networks and other development actors.
NB: the main target already has a certain awareness of Vantor: we will try to minimize text to maximize visual impact and readability.
Secondary target:
Vantor will also distribute the brochure to new prospects of interest during the Meridian Forum.
Timing:
We will need to finalize the design and have the files by June 1st to allow time for print before the event.
Content:
The document should be concise, highly readable (no clutter) and include:
1. text (that we will provide)
and
2. visual elements such as images, shapes and info-graphics (that is you).
NB: Vantor does not have its own image bank; photos will be provided by you.
Format:
A4 folded in half - 4pp A5 - PORTRAIT FORMAT) with an impactful visual in the front, logo, title and headline (please see examples in the mood board attached).
Design elements:
Vantor does not have yet a visual identity (please see: http://vantor.org) so there is room for creativity and no graphic chart to follow.
The sector of consulting in international development is rather conservative but our intention is to be disruptive and create a “Wow” effect. We count on you for that!
Therefore, the design should be “structured”, “organized”, “uncluttered” but also “modern”, “impactful”, “highly visual” (think infographic or mind map to describe our services and projects).
Please, take the time to see the attached presentation: I give you guidelines and examples of what we want and what we like.
We are looking forward to seeing your work and I am available for comments, questions and support.
Thank you.
RK
Target Market(s)
The full brief is in the project description: please, scroll through it.
The target market is : our existing clients base, working in sustainable development (read: NGO and United Nations people)
Industry/Entity Type
Ngo
Font styles to use
Requirements
Must have
- - Design and color elements: please, no black and white. Our company website is in black and white and without graphics; we want the brochure to break away from that and start creating our brand identity; so please, show us colors and desing elements (shapes, backgrounds, etc).
- You have a chance to showcase your talent in terms of visual identity: what lines, forms, layout and colors can you come up with and apply throughout the brochure and serve as the visual identity of Vantor?
- The structure of the document should be:
- - Front cover: design elements + impacful photo (see mood board example attached) +our logo + this headline: "Collective action for sustainable development and impact"
- - Inside front: a graphic representation of "Our Services": such as core activity in the center circle and satellite circles for the services we offer.
- - Inside back:
- 1. Icons and text boxes for "Our projects"
- 2. A world map of the countries where we have worked. Full list of countries is here:
- http://vantor.org/experience-1
- - Back cover: our contact + logos of partners.
- Our partners are listed here:
- Please use their original logos (ie, in color).
- The design we will select will serve as a basis for a graphic chart...so more work to come...word to the wise ;)
- Please check out our website vantor.org to see what we do etc.
Nice to have
- Icons to reflect our services: what icons can you come up with to describe "training services", "building networks" or "program management"?
- I give examples in the mood board.
Should not have
- We are open to creativity and want to generate a "Wow" effect.
- Just note that the sector is rather conservative so flashy colors and cartoon like characters should be avoided. Think "earth, global change, United Nations, climate" without going too green (it's overdone). ;-)
- Make us stand out in the NGO world
- Now you.

```html
<!DOCTYPE html>
<html lang="en">
<head>
<meta charset="utf-8">
<title>Vantor – Brochure spreads</title>
<link href="https://fonts.googleapis.com/css2?family=Ubuntu:wght@300;400;500;700&display=swap" rel="stylesheet">
<style>
:root{
  --bg:#e9e9e7;
  --paper:#ffffff;
  --navy:#3d5170;
  --navy-dark:#3a4963;
  --gold:#e7b25b;
  --gold-text:#e0a544;
  --red:#c1343b;
  --green:#6b9a3c;
  --blue:#5b88bd;
  --yellow:#eed14f;
  --brown:#5c4b3f;
  --ink:#4a4a4a;
}
*{margin:0;padding:0;box-sizing:border-box}
html,body{width:860px;height:1200px;overflow:hidden;background:var(--bg)}
body{position:relative;font-family:"Ubuntu",sans-serif;color:var(--ink)}
.spread{position:absolute;left:72px;width:716px;height:500px;background:var(--paper);box-shadow:0 3px 12px rgba(0,0,0,.18)}
.spread--outer{top:66px}
.spread--inner{top:630px}
.page{position:absolute;top:0;width:358px;height:100%}
.page--left{left:0}
.page--right{left:358px}
.fold{position:absolute;left:352px;top:0;width:12px;height:100%;background:linear-gradient(90deg,rgba(0,0,0,0) 0,rgba(0,0,0,.07) 50%,rgba(0,0,0,0) 100%);z-index:5}
.stripe{position:absolute;left:0;bottom:0;width:100%;height:4px;display:flex}
.stripe span{flex:1}
.brand{position:absolute;top:30px;left:12px;font-size:36px;font-weight:400;color:#6d6d6d;letter-spacing:.5px}
.band{position:absolute;top:73px;left:0;width:716px;height:295px}
.projects{position:absolute;top:73px;left:0;width:300px;padding:38px 0 0 13px;color:#fff}
.projects h3{color:var(--gold);font-size:10.5px;font-weight:500;margin-bottom:16px}
.projects li{list-style:none;position:relative;padding-left:13px;font-size:7.3px;line-height:1.28;font-weight:300;margin-bottom:10px}
.projects li::before{content:"";position:absolute;left:1px;top:2px;width:5px;height:5px;background:var(--gold)}
.contact{position:absolute;top:398px;left:13px}
.contact h3{color:var(--red);font-size:12px;font-weight:400;margin-bottom:12px}
.contact p{display:flex;align-items:center;font-size:12.5px;font-weight:300;color:#444;margin-bottom:9px}
.contact svg{margin-right:12px}
.divider{position:absolute;left:207px;top:386px;width:1px;height:86px;background:#ccc}
.supporters{position:absolute;top:390px;left:214px;width:140px;font-size:6.4px;line-height:1.3;color:#555}
.badges{display:flex;flex-wrap:wrap;gap:5px 6px;margin-top:8px;align-items:center}
.badge{width:30px;height:16px;background:#d6dce6}
.badge--blue{background:#2e4a9a}
.badge--round{width:18px;height:18px;border-radius:50%;background:#b9c8dc}
.headline{position:absolute;top:436px;left:378px;color:var(--navy);font-size:15.5px;font-weight:700;line-height:1.42;letter-spacing:.2px}
.section-bar{position:absolute;top:0;height:55px;width:358px;background:var(--gold);color:#fff;font-size:15px;font-weight:500;padding:30px 0 0 14px}
.question{position:absolute;top:72px;left:14px;width:300px;color:var(--red);font-size:7.4px;line-height:1.4}
.body-text{position:absolute;top:102px;left:14px;width:328px;font-size:7.4px;line-height:1.45;text-align:justify;font-weight:300;color:#444}
.map{position:absolute;top:196px;left:12px;width:330px;height:160px}
.list-col{position:absolute;top:372px;font-size:7.2px;color:#444;font-weight:300}
.list-col h4{color:var(--gold-text);font-size:9.5px;font-weight:400;margin-bottom:6px}
.list-col li{list-style:none;position:relative;padding-left:10px;line-height:1.55}
.list-col li::before{content:"";position:absolute;left:0;top:3px;width:5px;height:5px;background:var(--gold)}
.intro{position:absolute;top:72px;left:10px;width:338px;font-size:7.4px;line-height:1.45;text-align:justify;color:#444;font-weight:300}
.services{position:absolute;top:125px;left:0;width:358px;height:270px}
.tile{position:absolute;width:80px;height:58px;border-radius:7px;color:#fff;font-size:6.2px;text-align:center;line-height:1.25;display:flex;flex-direction:column;align-items:center;justify-content:flex-end;padding-bottom:7px;box-shadow:0 3px 4px rgba(0,0,0,.18)}
.tile svg{margin-bottom:5px}
.tile--research{left:34px;top:11px;background:var(--gold)}
.tile--training{left:138px;top:11px;background:var(--red)}
.tile--knowledge{left:223px;top:11px;background:var(--green)}
.tile--coalition{left:34px;top:202px;background:var(--blue)}
.tile--evaluation{left:138px;top:202px;background:var(--yellow)}
.tile--communication{left:223px;top:202px;background:var(--navy-dark)}
.hub{position:absolute;left:92px;top:110px;width:164px;height:48px;border-radius:24px;background:var(--brown);color:#fff;font-size:30px;font-weight:400;text-align:center;line-height:48px;box-shadow:0 3px 5px rgba(0,0,0,.25)}
.closing{position:absolute;top:438px;left:40px;width:290px;text-align:center;color:var(--gold-text);font-size:7.2px;line-height:1.35}
</style>
</head>
<body>

<section class="spread spread--outer">
  <div class="page page--left">
    <div class="brand">Vantor</div>
  </div>
  <div class="page page--right">
    <div class="brand">Vantor</div>
  </div>

  <svg class="band" viewBox="0 0 716 295">
    <defs>
      <linearGradient id="photoTone" x1="0" y1="0" x2="1" y2="1">
        <stop offset="0" stop-color="#2f4a78"/>
        <stop offset=".35" stop-color="#9fc0df"/>
        <stop offset=".6" stop-color="#e9f1f7"/>
        <stop offset=".85" stop-color="#7d6a55"/>
        <stop offset="1" stop-color="#3b4e6d"/>
      </linearGradient>
    </defs>
    <rect x="0" y="0" width="360" height="295" fill="#3d5170"/>
    <path d="M336 6 L716 6 L716 290 L302 290 Q318 150 336 6 Z" fill="url(#photoTone)" role="img" aria-label="Photograph looking up through a curved glass staircase toward a bright skylight"/>
  </svg>

  <div class="projects">
    <h3>PROJECTS:</h3>
    <ul>
      <li>Advising Tessaly Aid in the elaboration of their donor diversification strategy</li>
      <li>Assisting Solvera Foundation with the review of the intervention guide of Socivia+ and methodological support to conduct policy dialogue at country level (Continental Union–Latin America)</li>
      <li>Conducting the mid term evaluation of the multi-country programme PRAXOR (strengthening democratic governance and rule of law in Southeast and Eastern Europe) for the Lowland Rights Committee</li>
      <li>Conceptualizing and implementing policy dialogues at country level for the Continental Union funded programme Climavera+</li>
      <li>Contributing with content, analysis and facilitation to the Open Forum for Progress, a Continental Union funded multi-stakeholder platform</li>
      <li>Feeding the public debate with blogs and specialized articles in relevant media outlets and think tanks, like La Gaceta Azul, Geolumen Hub and Instituto Ondrava</li>
    </ul>
  </div>

  <div class="contact">
    <h3>CONTACT US</h3>
    <p>
      <svg width="20" height="20" viewBox="0 0 20 20"><circle cx="10" cy="10" r="10" fill="#c1343b"/><rect x="5" y="6.5" width="10" height="7" fill="none" stroke="#fff" stroke-width="1.2"/><path d="M5 6.5 L10 10.5 L15 6.5" fill="none" stroke="#fff" stroke-width="1.2"/></svg>
      info@vantor.org
    </p>
    <p>
      <svg width="20" height="20" viewBox="0 0 20 20"><circle cx="10" cy="10" r="10" fill="#c1343b"/><circle cx="10" cy="10" r="5.5" fill="none" stroke="#fff" stroke-width="1.1"/><ellipse cx="10" cy="10" rx="2.4" ry="5.5" fill="none" stroke="#fff" stroke-width="1"/><line x1="4.5" y1="10" x2="15.5" y2="10" stroke="#fff" stroke-width="1"/></svg>
      www.vantor.org
    </p>
  </div>

  <div class="divider"></div>
  <div class="supporters">
    Vantor supports the work of:<br>Continental Union, World Assembly, Oberwind Agency, Solvera Foundation, Tessaly Aid, Calloway School
    <div class="badges">
      <span class="badge badge--blue"></span>
      <span class="badge"></span>
      <span class="badge"></span>
      <span class="badge badge--round"></span>
      <span class="badge"></span>
      <span class="badge"></span>
      <span class="badge"></span>
      <span class="badge badge--round"></span>
    </div>
  </div>

  <div class="headline">PROMOTING COLLECTIVE ACTION<br>FOR SUSTAINABLE DEVELOPMENT</div>

  <div class="fold"></div>
  <div class="stripe">
    <span style="background:#2d4b8e"></span><span style="background:#e7b25b"></span><span style="background:#6b9a3c"></span><span style="background:#c1343b"></span><span style="background:#5b88bd"></span><span style="background:#eed14f"></span><span style="background:#3a4963"></span><span style="background:#d9418a"></span><span style="background:#f08a2c"></span><span style="background:#4bb3c9"></span><span style="background:#8a2e52"></span><span style="background:#e23b2e"></span>
  </div>
</section>

<section class="spread spread--inner">
  <div class="page page--left">
    <div class="section-bar">OUR FIELD</div>
    <p class="question">Is it possible to deliver effective solutions in the 21st Century without well-managed collaborative action?</p>
    <p class="body-text">In Vantor we consider that, both individually and collectively, we are evolving towards more complex and mixed forms of interaction and organization. Our view is that the intellectual effort to understand that evolution needs to be combined with the practical capacity to take advantage of its great potential: the construction of realistic schemes and environments where both citizens and organizations can participate critically and contribute effectively to the public good.</p>
    <div class="map" role="img" aria-label="Dotted world map with location pins marking countries where Vantor has worked" style="background:radial-gradient(ellipse at 50% 50%,#c9d5ea 0,#e6ecf5 55%,#ffffff 80%)"></div>
    <div class="list-col" style="left:14px">
      <h4>We specialize in:</h4>
      <ul>
        <li>Policy dialogue</li>
        <li>Donor diversification strategies</li>
        <li>Multi-stakeholder partnerships</li>
        <li>Strategic partnerships</li>
        <li>Framework agreements</li>
        <li>Goal-directed networks</li>
      </ul>
    </div>
    <div class="list-col" style="left:182px">
      <h4>We work with:</h4>
      <ul>
        <li>International Organizations</li>
        <li>Private sector companies</li>
        <li>NGOs</li>
        <li>Trade unions</li>
        <li>Universities and Think tanks</li>
        <li>Regional and Local governments</li>
        <li>Development agencies</li>
      </ul>
    </div>
  </div>

  <div class="page page--right">
    <div class="section-bar">Vantor services</div>
    <p class="intro">Vantor is a response to the growing need of a wide array of organizations to understand changes in the development landscape, undergo structural changes, improve processes and increase the impact of their participation in collective actions to attain development goals.</p>

    <div class="services">
      <svg width="358" height="270" viewBox="0 0 358 270" style="position:absolute;left:0;top:0">
        <path d="M100 104 A88 40 0 0 0 100 164" fill="none" stroke="#bbb" stroke-width="2"/>
        <path d="M248 104 A88 40 0 0 1 248 164" fill="none" stroke="#bbb" stroke-width="2"/>
        <g fill="none" stroke="#aaa" stroke-width="1.2">
          <path d="M74 80 V90 H160 V108"/>
          <path d="M178 80 V108"/>
          <path d="M263 80 V90 H196 V108"/>
          <path d="M160 160 V178 H74 V190"/>
          <path d="M178 160 V190"/>
          <path d="M196 160 V178 H263 V190"/>
        </g>
        <g>
          <circle cx="74" cy="80" r="2" fill="#e7b25b"/><circle cx="178" cy="80" r="2" fill="#c1343b"/><circle cx="263" cy="80" r="2" fill="#5b88bd"/>
          <circle cx="178" cy="94" r="2" fill="#c1343b"/>
          <circle cx="160" cy="166" r="2" fill="#5b88bd"/><circle cx="178" cy="166" r="2" fill="#e7b25b"/><circle cx="196" cy="166" r="2" fill="#333"/>
        </g>
      </svg>

      <div class="tile tile--research">
        <svg width="20" height="20" viewBox="0 0 20 20"><circle cx="10" cy="10" r="8" fill="none" stroke="#fff" stroke-width="1.6"/><circle cx="10" cy="10" r="4.5" fill="none" stroke="#fff" stroke-width="1.6"/><circle cx="10" cy="10" r="1.5" fill="#fff"/><path d="M10 10 L18 2" stroke="#fff" stroke-width="1.4"/></svg>
        RESEARCH AND<br>ANALYSIS
      </div>
      <div class="tile tile--training">
        <svg width="20" height="20" viewBox="0 0 20 20"><rect x="3" y="6" width="6" height="12" fill="#fff"/><rect x="10" y="2" width="7" height="16" fill="#fff"/><g fill="#c1343b"><rect x="11.5" y="4" width="1.5" height="2"/><rect x="14" y="4" width="1.5" height="2"/><rect x="11.5" y="8" width="1.5" height="2"/><rect x="14" y="8" width="1.5" height="2"/><rect x="4.5" y="9" width="1.5" height="2"/></g></svg>
        FACILITATION AND<br>TRAINING
      </div>
      <div class="tile tile--knowledge">
        <svg width="20" height="20" viewBox="0 0 20 20"><circle cx="8" cy="11" r="4.5" fill="none" stroke="#fff" stroke-width="2.2" stroke-dasharray="2 1.5"/><circle cx="8" cy="11" r="1.6" fill="#fff"/><circle cx="15" cy="5" r="3" fill="none" stroke="#fff" stroke-width="1.8" stroke-dasharray="1.6 1.2"/></svg>
        KNOWLEDGE<br>MANAGEMENT
      </div>

      <div class="hub">Vantor</div>

      <div class="tile tile--coalition">
        <svg width="20" height="20" viewBox="0 0 20 20"><circle cx="7" cy="4" r="2.2" fill="#fff"/><circle cx="14" cy="7" r="2.2" fill="#fff"/><path d="M3 17 L7 9 L10 13 L14 11 L17 17 Z" fill="#fff"/></svg>
        COALITION<br>BUILDING
      </div>
      <div class="tile tile--evaluation">
        <svg width="20" height="20" viewBox="0 0 20 20"><rect x="3" y="5" width="14" height="10" fill="none" stroke="#fff" stroke-width="1.6"/><path d="M5 13 L8 9 L11 11 L15 7" fill="none" stroke="#fff" stroke-width="1.4"/><rect x="7" y="16" width="6" height="1.6" fill="#fff"/></svg>
        EVALUATION
      </div>
      <div class="tile tile--communication">
        <svg width="20" height="20" viewBox="0 0 20 20"><rect x="4" y="12" width="2.4" height="5" fill="#fff"/><rect x="8" y="9" width="2.4" height="8" fill="#fff"/><rect x="12" y="6" width="2.4" height="11" fill="#fff"/><path d="M3 9 L8 5 L11 7 L17 2" fill="none" stroke="#fff" stroke-width="1.3"/></svg>
        COMMUNICATION
      </div>
    </div>

    <p class="closing">In Vantor we believe that theory cannot be separated from practice. The real background of our work is trying to adapt models to a changing reality.</p>
  </div>

  <div class="fold"></div>
  <div class="stripe">
    <span style="background:#2d4b8e"></span><span style="background:#e7b25b"></span><span style="background:#6b9a3c"></span><span style="background:#c1343b"></span><span style="background:#5b88bd"></span><span style="background:#eed14f"></span><span style="background:#3a4963"></span><span style="background:#d9418a"></span><span style="background:#f08a2c"></span><span style="background:#4bb3c9"></span><span style="background:#8a2e52"></span><span style="background:#e23b2e"></span>
  </div>
</section>

</body>
</html>
```